Custom unique Stationary design for Logistics company

We need a custom, unique , elegant and luxurious full stationary design using our new logo, following these guidelines:
1- Business card: double sided, both sides uses the navy blue as the background main color (same as the code of the navy blue used in our logo).
2- envelope and folder: also use the same navy blue as the main background color.
3- book cover( notepad cover) : same thing with the navy blue
4- letterhead: feel free to use the combination of the colors in our logo.
5- rest of the items are up to your creativity

Target Market(s)

corporates and other businesses

Industry/Entity Type

Logistics and heavy machines contractors

Requirements
Must have
• Letterhead, business card, envelope, notepad cover, paper, file
Nice to have
• navy blue to be main background color for business card, envelope, notepad cover

```html
<!DOCTYPE html>
<html lang="en">
<head>
<meta charset="utf-8">
<title>Northway Freight Company – Envelope</title>
<link href="https://fonts.googleapis.com/css2?family=Montserrat:wght@400;600;800&display=swap" rel="stylesheet">
<style>
  :root {
    --navy: #084d70;
    --orange: #e85d2f;
    --paper: #f6f5f5;
    --backdrop: #d2d1d1;
    --ink: #1a1a1a;
    --tag-grey: #8f9396;
    --white: #ffffff;
  }
  * { margin: 0; padding: 0; box-sizing: border-box; }
  html, body {
    width: 1200px;
    height: 1050px;
    overflow: hidden;
    background: var(--backdrop);
    font-family: "Montserrat", Arial, sans-serif;
  }
  .canvas { position: relative; width: 1200px; height: 1050px; }
  .envelope {
    position: absolute;
    left: 145px;
    width: 910px;
    height: 390px;
    background: var(--paper);
    overflow: hidden;
  }
  .envelope--back { top: 105px; }
  .envelope--front { top: 555px; }
  .envelope svg { position: absolute; left: 0; top: 0; }
  .flap-brand {
    position: absolute;
    left: 0; top: 26px; width: 910px;
    text-align: center;
    color: var(--white);
  }
  .flap-brand .brand-name {
    font-weight: 800;
    font-size: 40px;
    letter-spacing: 2px;
    line-height: 1;
  }
  .flap-brand .brand-tagline {
    margin-top: 10px;
    font-weight: 800;
    font-size: 7px;
    letter-spacing: 0.6px;
  }
  .front-brand {
    position: absolute;
    left: 42px; top: 60px;
    width: 242px;
  }
  .front-brand .brand-name {
    color: var(--navy);
    font-weight: 800;
    font-size: 54px;
    letter-spacing: 1px;
    line-height: 1;
    white-space: nowrap;
  }
  .front-brand .brand-tagline {
    margin-top: 14px;
    color: var(--tag-grey);
    font-weight: 800;
    font-size: 9.5px;
    letter-spacing: 0.5px;
    white-space: nowrap;
  }
  .return-address {
    position: absolute;
    left: 41px; top: 183px;
    color: var(--ink);
    font-size: 15.5px;
    line-height: 20px;
    font-weight: 400;
  }
</style>
</head>
<body>
<main class="canvas">
  <section class="envelope envelope--back" aria-label="Envelope back">
    <svg width="910" height="390" viewBox="0 0 910 390" aria-hidden="true">
      <path class="flap" fill="var(--navy)" d="M0 0 H910 L884 92 Q868 131 826 131 H75 Q42 131 25 92 Z"/>
    </svg>
    <div class="flap-brand">
      <div class="brand-name">NORTHWAY</div>
      <div class="brand-tagline">NORTHWAY FREIGHT COMPANY</div>
    </div>
  </section>

  <section class="envelope envelope--front" aria-label="Envelope front">
    <svg width="910" height="390" viewBox="0 0 910 390" aria-hidden="true">
      <path class="wave-band" fill="var(--navy)" d="M0 292 C120 258 260 262 420 298 C560 330 680 362 780 334 C840 318 880 298 910 264 V390 H0 Z"/>
      <path class="wave-line" fill="none" stroke="var(--orange)" stroke-width="7" d="M0 292 C120 258 260 262 420 298 C560 330 680 362 780 334 C840 318 880 298 910 264"/>
    </svg>
    <div class="front-brand">
      <div class="brand-name">NORTHWAY</div>
      <div class="brand-tagline">NORTHWAY FREIGHT COMPANY</div>
    </div>
    <address class="return-address" style="font-style:normal">
      1420 Harbour Line, Unit 38<br>
      Brampton, ON L6T&nbsp;&nbsp;4K9
    </address>
  </section>
</main>
</body>
</html>
```